Modern business card for triathlon training business in Australia

We need a business card design for our triathlon training company.

Pace with Us Fitness is an Australian business, owned by women, run for women. Pace with Us Fitness helps women prepare or improve triathlon skills and confidence through triathlon camps completely designed for women.

Our camps focus on preparing women both physically and mentally for their next (or first!) triathlon.

You can see our website www.pacewithusfitness.com.au for more info about our business and our style.

We've attached two of our logos and are happy to consider a design that utilised either colour scheme with the teal colour being our 'feature' colour. We don't want overly feminine cards but rather cards that are professional and neat. If the inclusion of any pictures/art is warranted, this should be focused on our swim/ride/run theme and in that specific order (swim/ride/run).

The business card needs to be a printable design and the contact details will need to change for our two employees.

Target Market(s)

Female clients and partners/vendors/sponsors that we work with in the triathlon industry

Industry/Entity Type

Fitness

Contact Information for Business Card

Pace with Us Fitness (business name)
Nina Carver
Business Director
Mobile: 0438 916 207
Email: nina@pacewithusfitness.com.au
www.pacewithusfitness.com.au

Second business card:
Pace with Us Fitness
Bel Stray
Coaching Director
Mobile: 0459 260 718
Email: bel@pacewithusfitness.com.au

Font styles to use
Serif
Sans Serif

Requirements
Must have
• Core contact details above, our logo and be a printable design
Should not have
• Pink
• Cursive/script fonts

```html
<!DOCTYPE html>
<html lang="en">
<head>
<meta charset="utf-8">
<title>Pace with Us Fitness – Business Cards</title>
<link rel="stylesheet" href="https://fonts.googleapis.com/css2?family=Questrial&family=Open+Sans:wght@400;600&display=swap">
<style>
  :root {
    --teal: #1dbdcf;
    --teal-soft: #5fd3e0;
    --white: #ffffff;
    --backdrop: #e6e7e8;
    --card-edge: rgba(0,0,0,0.18);
  }
  html, body {
    margin: 0;
    padding: 0;
    width: 1200px;
    height: 1200px;
    overflow: hidden;
    background: var(--backdrop);
  }
  .canvas {
    position: relative;
    width: 1200px;
    height: 1200px;
  }
  .card {
    position: absolute;
    left: 288px;
    width: 655px;
    height: 405px;
    background: var(--white);
    box-shadow: 0 1px 3px var(--card-edge);
    overflow: hidden;
  }
  .card--nina { top: 116px; }
  .card--bel { top: 623px; }
  .brand-panel {
    position: absolute;
    left: 0;
    top: 0;
    width: 266px;
    height: 100%;
    background: var(--teal);
    display: flex;
    align-items: center;
    justify-content: center;
  }
  .brand-name {
    margin: 0;
    margin-top: -30px;
    width: 200px;
    text-align: center;
    color: var(--white);
    font-family: "Questrial", sans-serif;
    font-size: 30px;
    line-height: 1.15;
    font-weight: 400;
  }
  .sport-art {
    position: absolute;
    left: 266px;
    top: 52px;
    width: 84px;
    height: 330px;
    background: linear-gradient(180deg, var(--teal) 0%, var(--teal-soft) 50%, var(--teal) 100%);
    border-radius: 0 40px 40px 0;
    opacity: 0.85;
  }
  .person-name {
    position: absolute;
    right: 40px;
    top: 84px;
    max-width: 240px;
    margin: 0;
    color: var(--teal);
    font-family: "Questrial", sans-serif;
    font-size: 42px;
    font-weight: 400;
    letter-spacing: 0.5px;
    line-height: 1;
    white-space: nowrap;
    text-align: right;
  }
  .person-role {
    position: absolute;
    right: 42px;
    top: 140px;
    margin: 0;
    color: var(--teal);
    font-family: "Open Sans", sans-serif;
    font-size: 17px;
    font-weight: 400;
  }
  .contact-list {
    position: absolute;
    left: 384px;
    top: 250px;
    margin: 0;
    padding: 0;
    list-style: none;
  }
  .contact-item {
    display: flex;
    align-items: center;
    height: 17px;
    margin-bottom: 17px;
    color: var(--teal);
    font-family: "Open Sans", sans-serif;
    font-weight: 600;
    font-size: 11px;
    letter-spacing: 1.8px;
    white-space: nowrap;
  }
  .contact-item--phone {
    font-size: 13.5px;
    letter-spacing: 2.4px;
  }
  .contact-icon {
    width: 16px;
    height: 16px;
    margin-right: 9px;
    flex: none;
  }
</style>
</head>
<body>
<main class="canvas">

  <section class="card card--nina">
    <div class="brand-panel"><p class="brand-name">Pace with Us Fitness</p></div>
    <div class="sport-art" role="img" aria-label="Silhouettes of a swimmer, a cyclist and a runner in sequence"></div>
    <h1 class="person-name">Nina Carver</h1>
    <p class="person-role">Business Director</p>
    <ul class="contact-list">
      <li class="contact-item contact-item--phone">
        <svg class="contact-icon" viewBox="0 0 16 16" fill="none" stroke="#1dbdcf" stroke-width="1.2"><circle cx="8" cy="8" r="7"/><path d="M5.5 4.5l1.3 0.2 0.6 1.6-0.9 0.8a5 5 0 0 0 2.4 2.4l0.8-0.9 1.6 0.6 0.2 1.3c-0.6 0.6-1.6 0.8-2.4 0.4a8 8 0 0 1-3.9-3.9c-0.4-0.8-0.2-1.8 0.3-2.5z" fill="#1dbdcf" stroke="none"/></svg>
        0438 916 207
      </li>
      <li class="contact-item">
        <svg class="contact-icon" viewBox="0 0 16 16" fill="none" stroke="#1dbdcf" stroke-width="1.2"><circle cx="8" cy="8" r="7"/><rect x="4.2" y="5.3" width="7.6" height="5.4"/><path d="M4.2 5.3L8 8.3l3.8-3"/></svg>
        nina@pacewithusfitness.com.au
      </li>
      <li class="contact-item">
        <svg class="contact-icon" viewBox="0 0 16 16" fill="none" stroke="#1dbdcf" stroke-width="1.2"><circle cx="8" cy="8" r="7"/><ellipse cx="8" cy="8" rx="3" ry="7"/><path d="M1 8h14M2 4.5h12M2 11.5h12"/></svg>
        www.pacewithusfitness.com.au
      </li>
    </ul>
  </section>

  <section class="card card--bel">
    <div class="brand-panel"><p class="brand-name">Pace with Us Fitness</p></div>
    <div class="sport-art" role="img" aria-label="Silhouettes of a swimmer, a cyclist and a runner in sequence"></div>
    <h1 class="person-name">Bel Stray</h1>
    <p class="person-role">Coaching Director</p>
    <ul class="contact-list">
      <li class="contact-item contact-item--phone">
        <svg class="contact-icon" viewBox="0 0 16 16" fill="none" stroke="#1dbdcf" stroke-width="1.2"><circle cx="8" cy="8" r="7"/><path d="M5.5 4.5l1.3 0.2 0.6 1.6-0.9 0.8a5 5 0 0 0 2.4 2.4l0.8-0.9 1.6 0.6 0.2 1.3c-0.6 0.6-1.6 0.8-2.4 0.4a8 8 0 0 1-3.9-3.9c-0.4-0.8-0.2-1.8 0.3-2.5z" fill="#1dbdcf" stroke="none"/></svg>
        0438 916 207
      </li>
      <li class="contact-item">
        <svg class="contact-icon" viewBox="0 0 16 16" fill="none" stroke="#1dbdcf" stroke-width="1.2"><circle cx="8" cy="8" r="7"/><rect x="4.2" y="5.3" width="7.6" height="5.4"/><path d="M4.2 5.3L8 8.3l3.8-3"/></svg>
        bel@pacewithusfitness.com.au
      </li>
      <li class="contact-item">
        <svg class="contact-icon" viewBox="0 0 16 16" fill="none" stroke="#1dbdcf" stroke-width="1.2"><circle cx="8" cy="8" r="7"/><ellipse cx="8" cy="8" rx="3" ry="7"/><path d="M1 8h14M2 4.5h12M2 11.5h12"/></svg>
        www.pacewithusfitness.com.au
      </li>
    </ul>
  </section>

</main>
</body>
</html>
```